Copper Ridge Garage Door Sales & Repair needs a Business Card Design

I need a business card design to go with our new business logo that was created a few months ago.

Copper Ridge Garage Door specializes in selling and installing new garage doors, and new garage door openers. We also take care of all repairs to existing garage doors and garage door openers. All makes and models.

Target Market(s)

Home-owners, renters, anyone who lives in a house and has a garage. Residential and commercial garages.

Industry/Entity Type

Home Improvement

Contact Information for Business Card

I would like the business cards to have rounded corners and be double-sided. My old logo is still on my website at www.copperridgegarage.example. If I was going to incorporate a secondary color on the business cards, I think that orange is a good choice (especially since blue and orange are the colors of our Tulsa Kestrels), but I'm not opposed to seeing a different color if another color works better with my logo colors. I have two logo colors. One designed for a white background and one designed for a darker background. I'm not opposed to using both. Maybe a dark background with the white logo on one side, and a white background with the other logo color on the other side.

My business is a small, locally owned business that I am trying to grow. But I would like my business cards to look very professional. Like we have been in business for a long time. I like traditional to modern looking cards. Just something bold and memorable. My full company name is Copper Ridge Garage Door Sales & Repair. But you can just do COPPER RIDGE GARAGE DOOR, if that works better.

Font styles to use
Serif
Script

Requirements
Must have
• Rounded corners
• Double-sided
• 3-D Elements. Layering of some sort (a sketch of a garage door or a 3rd color (orange) brought in some how. I really like watermarks.
• Matte cards that you can write on.
• White on one side. (Or the lighter blue in my logo). Darker blue logo color on the other side.
• I would like our tag line on the cards somewhere... "For All Your Garage Door Needs".
• I would also like "Call For a FREE Estimate" by the phone number.
• And "Serving the Greater Metro Denver Area" somewhere on the card as well.
Nice to have
• Refer to "Business Card Details" above.

```html
<!DOCTYPE html>
<html lang="en">
<head>
<meta charset="utf-8">
<title>Copper Ridge Garage Doors – Business Card</title>
<link rel="stylesheet" href="https://fonts.googleapis.com/css2?family=Crimson+Text:ital,wght@0,400;0,700;1,400&display=swap">
<style>
  :root {
    --stage: #2b2b2e;
    --navy: #3b4b72;
    --navy-deep: #2f3d5f;
    --ink: #2c3a5e;
    --pale-blue: #cdd9e6;
    --paper: #f7f7f8;
    --paper-shade: #e9e9ec;
    --rule: #111218;
    --text-muted: #555a66;
  }
  * { box-sizing: border-box; margin: 0; padding: 0; }
  html, body {
    width: 1200px; height: 873px; overflow: hidden;
    background: var(--stage);
    font-family: "Crimson Text", Georgia, serif;
  }
  .stage {
    position: relative; width: 1200px; height: 873px;
    display: flex; align-items: center; justify-content: center; gap: 60px;
  }
  .card {
    position: relative; width: 525px; height: 300px;
    border-radius: 16px; overflow: hidden;
  }
  /* Back side */
  .card--back {
    background: linear-gradient(160deg, var(--navy) 0%, var(--navy-deep) 100%);
    display: flex; flex-direction: column; align-items: center; justify-content: center;
  }
  .brand-name {
    text-align: center; font-weight: 700; text-transform: uppercase; line-height: 1.05;
  }
  .card--back .brand-name { color: var(--pale-blue); font-size: 34px; letter-spacing: 1px; }
  .card--back .brand-name small { display: block; font-size: 18px; letter-spacing: 4px; margin-top: 6px; }
  .tagline {
    margin-top: 16px; color: var(--pale-blue);
    font-size: 17px; font-style: italic; letter-spacing: 0.5px;
  }

  /* Front side */
  .card--front {
    background: linear-gradient(160deg, var(--paper) 0%, var(--paper-shade) 100%);
  }
  .card--front .brand {
    position: absolute; left: 24px; top: 62px; width: 210px; height: 120px;
    display: flex; align-items: center; justify-content: center;
  }
  .card--front .brand-name { color: var(--ink); font-size: 28px; }
  .card--front .brand-name small { display: block; font-size: 15px; letter-spacing: 3px; margin-top: 5px; }
  .divider {
    position: absolute; left: 250px; top: 36px; width: 2px; height: 170px;
    background: linear-gradient(to bottom, rgba(44,58,94,0.9), rgba(44,58,94,0));
  }
  .person { position: absolute; left: 280px; top: 48px; }
  .person-name { color: var(--ink); font-size: 21px; font-weight: 700; }
  .person-role { color: var(--text-muted); font-size: 12px; }
  .estimate-note {
    position: absolute; left: 280px; top: 112px;
    color: var(--ink); font-size: 13px; font-weight: 700; letter-spacing: 0.3px;
  }
  .contacts {
    position: absolute; left: 280px; top: 136px; list-style: none;
  }
  .contacts li {
    display: flex; align-items: center; gap: 8px;
    color: var(--ink); font-size: 13px; height: 24px;
  }
  .contacts svg { width: 18px; height: 18px; flex: none; }
  .band-rule {
    position: absolute; left: 0; right: 0; bottom: 56px; height: 5px; background: var(--rule);
  }
  .band {
    position: absolute; left: 0; right: 0; bottom: 0; height: 52px; background: var(--navy);
    display: flex; align-items: center; justify-content: center;
  }
  .service-area {
    color: var(--pale-blue); font-size: 15px; letter-spacing: 1.5px;
  }
</style>
</head>
<body>
<main class="stage">
  <section class="card card--back" aria-label="Card back">
    <div class="brand-name">Copper Ridge<br>Garage<small>Doors</small></div>
    <p class="tagline">For All Your Garage Door Needs</p>
  </section>

  <section class="card card--front" aria-label="Card front">
    <div class="brand">
      <div class="brand-name">Copper Ridge<br>Garage<small>Doors</small></div>
    </div>
    <div class="divider"></div>
    <div class="person">
      <p class="person-name">Owen Callder</p>
      <p class="person-role">Owner / Founder</p>
    </div>
    <p class="estimate-note">Call For a FREE Estimate</p>
    <ul class="contacts">
      <li>
        <svg viewBox="0 0 18 18"><circle cx="9" cy="9" r="9" fill="var(--ink)"/><path d="M6 4.5c.6 0 1.4 1.6 1.4 2.1 0 .6-.9.8-.7 1.4.4 1 1.3 1.9 2.3 2.3.6.2.8-.7 1.4-.7.5 0 2.1.8 2.1 1.4 0 .9-1 1.6-1.9 1.6C8 12.6 5.4 10 5.4 7c0-.9.6-2.5.6-2.5z" fill="#fff"/></svg>
        +44 (0) 7700 900214
      </li>
      <li>
        <svg viewBox="0 0 18 18"><circle cx="9" cy="9" r="9" fill="var(--ink)"/><rect x="4.5" y="6" width="9" height="6.5" fill="none" stroke="#fff" stroke-width="1"/><path d="M4.5 6l4.5 3.8L13.5 6" fill="none" stroke="#fff" stroke-width="1"/></svg>
        owen@copperridgegarage.example
      </li>
      <li>
        <svg viewBox="0 0 18 18"><circle cx="9" cy="9" r="9" fill="var(--ink)"/></svg>
        social.example/copperridgegaragedoors
      </li>
    </ul>
    <div class="band-rule"></div>
    <div class="band">
      <p class="service-area">Serving the Greater Metro Denver Area</p>
    </div>
  </section>
</main>
</body>
</html>
```